Creative, Colorful, Dynamic Infographic for Global Non-Profit

We are a global arts and education non-profit in need of an infographic that illustrates four key skills embedded in our work: Curiosity, Listening, Imagination, Postive Action.
We work primarily with educators, students, and artists who use the power of personal stories to build community and connection and to bridge divides.
Our new brand guidelines, logos, and fonts are here: https://stylekit.example/quillbridge-7
I've attached a mock-up of the graphic and the required text. (Note the attached design was created by a staff person, your final design does not need to be the same. The color scheme and text of the final design should match the brand guidelines above.)
The graphic will be used for both web and print media and should include the purple Quillbridge 7 logo (also attached).
Ideally the final design will delight audiences and spark interest in our work.

```html
<!DOCTYPE html>
<html lang="en">
<head>
<meta charset="utf-8">
<title>Quillbridge 7 — Four Skills</title>
<link rel="stylesheet" href="https://fonts.googleapis.com/css2?family=Ubuntu:wght@400;500;700&display=swap">
<style>
  :root {
    --red: #ef4444;
    --purple: #653296;
    --yellow: #e8c22a;
    --green: #62b09a;
    --ink: #333333;
    --line: #777777;
    --paper: #ffffff;
  }
  html, body {
    margin: 0;
    padding: 0;
    width: 1200px;
    height: 1200px;
    overflow: hidden;
    background: var(--paper);
  }
  .skills-wheel {
    display: block;
    width: 1200px;
    height: 1200px;
    font-family: "Ubuntu", sans-serif;
  }
  .arc { fill: none; stroke-width: 50; stroke-linecap: round; }
  .arc--red { stroke: var(--red); }
  .arc--purple { stroke: var(--purple); }
  .arc--yellow { stroke: var(--yellow); }
  .arc--green { stroke: var(--green); }
  .outline { fill: none; stroke: var(--line); stroke-width: 3; }
  .outline--dashed { stroke-dasharray: 14 10; stroke-width: 5; }
  .node { fill: var(--paper); stroke: var(--line); stroke-width: 6; }
  .pointer { stroke: var(--line); stroke-width: 2.5; }
  .skill-title { font-weight: 700; font-size: 50px; text-anchor: middle; }
  .skill-title--red { fill: var(--red); }
  .skill-title--purple { fill: var(--purple); }
  .skill-title--yellow { fill: var(--yellow); }
  .skill-title--green { fill: var(--green); }
  .skill-text { fill: var(--ink); text-anchor: middle; font-size: 40px; font-weight: 500; }
  .skill-text--light { font-weight: 400; font-size: 46px; }
  .skill-text--large { font-weight: 700; font-size: 44px; }
  .caption { fill: var(--ink); font-size: 27px; text-anchor: middle; }
  .brand-name { fill: var(--purple); font-weight: 700; font-size: 92px; text-anchor: middle; }
</style>
</head>
<body>
<svg class="skills-wheel" viewBox="0 0 1932 1932" xmlns="http://www.w3.org/2000/svg">
  <defs>
    <radialGradient id="hub-shade" cx="0.4" cy="0.35" r="0.75">
      <stop offset="0" stop-color="#ffffff"/>
      <stop offset="0.7" stop-color="#f1f1f1"/>
      <stop offset="1" stop-color="#e2e2e2"/>
    </radialGradient>
  </defs>

  <!-- Central hub -->
  <g class="hub">
    <circle cx="965" cy="965" r="372" fill="#f4f4f4" stroke="#e6e6e6" stroke-width="4"/>
    <circle cx="965" cy="965" r="345" fill="url(#hub-shade)"/>
    <text class="brand-name" x="965" y="995">Quillbridge 7</text>
  </g>

  <!-- Positive action panel -->
  <g class="panel panel--action">
    <path class="outline outline--dashed" d="M578,240 C555,285 580,320 620,392"/>
    <path class="outline" d="M644,425 L722,552 C740,580 770,590 795,578 Q965,500 1135,575 C1160,585 1185,575 1198,550 L1270,425"/>
    <path class="outline outline--dashed" d="M1290,392 C1330,320 1360,285 1338,235"/>
    <path class="arc arc--red" d="M590,222 Q965,49 1325,212"/>
    <circle class="node" cx="635" cy="410" r="18"/>
    <circle class="node" cx="1280" cy="410" r="18"/>
    <line class="pointer" x1="618" y1="420" x2="575" y2="448"/>
    <line class="pointer" x1="1297" y1="420" x2="1345" y2="452"/>
    <circle cx="972" cy="218" r="18" fill="var(--ink)"/>
    <path d="M962,218 L969,226 L983,210" fill="none" stroke="#fff" stroke-width="4"/>
    <rect x="924" y="240" width="74" height="24" rx="10" fill="var(--ink)" role="img" aria-label="Open hand offering icon"/>
    <text class="skill-title skill-title--red" x="962" y="316">Positive action:</text>
    <text class="skill-text skill-text--light" x="962" y="380">Show your words</text>
    <text class="skill-text skill-text--light" x="962" y="443">and actions</text>
    <text class="skill-text skill-text--light" x="962" y="506">matter</text>
  </g>

  <!-- Curiosity panel -->
  <g class="panel panel--curiosity">
    <path class="outline outline--dashed" d="M222,598 C250,560 275,565 310,585 L385,628"/>
    <path class="outline" d="M420,652 L552,728 C578,745 590,772 578,800 Q520,965 578,1132 C590,1160 578,1185 552,1202 L420,1280"/>
    <path class="outline outline--dashed" d="M385,1302 L310,1345 C275,1365 250,1370 222,1335"/>
    <path class="arc arc--purple" d="M218,598 Q48,965 218,1335"/>
    <circle class="node" cx="402" cy="640" r="18"/>
    <circle class="node" cx="402" cy="1290" r="18"/>
    <line class="pointer" x1="415" y1="622" x2="432" y2="596"/>
    <line class="pointer" x1="414" y1="1310" x2="435" y2="1340"/>
    <rect x="308" y="760" width="90" height="117" rx="24" fill="var(--purple)" role="img" aria-label="Person with a bright idea icon"/>
    <text class="skill-title skill-title--purple" x="353" y="934">Curiosity:</text>
    <text class="skill-text" x="353" y="985">Focus on how</text>
    <text class="skill-text" x="353" y="1038">you can learn</text>
    <text class="skill-text" x="353" y="1090">from another's</text>
    <text class="skill-text" x="353" y="1142">knowledge and</text>
    <text class="skill-text" x="353" y="1195">experience</text>
  </g>

  <!-- Imagination panel -->
  <g class="panel panel--imagination">
    <path class="outline outline--dashed" d="M1710,598 C1682,560 1657,565 1622,585 L1535,636"/>
    <path class="outline" d="M1500,660 L1380,728 C1354,745 1342,772 1354,800 Q1410,965 1354,1132 C1342,1160 1354,1185 1380,1202 L1500,1272"/>
    <path class="outline outline--dashed" d="M1535,1296 L1622,1345 C1657,1365 1682,1370 1710,1335"/>
    <path class="arc arc--yellow" d="M1715,598 Q1881,965 1715,1335"/>
    <circle class="node" cx="1518" cy="647" r="18"/>
    <circle class="node" cx="1518" cy="1285" r="18"/>
    <line class="pointer" x1="1506" y1="628" x2="1487" y2="600"/>
    <line class="pointer" x1="1505" y1="1304" x2="1487" y2="1332"/>
    <rect x="1560" y="752" width="54" height="86" rx="20" fill="var(--yellow)" role="img" aria-label="Head with glowing mind icon"/>
    <text class="skill-title skill-title--yellow" x="1587" y="892">Imagination:</text>
    <text class="skill-text" x="1587" y="952">Consider</text>
    <text class="skill-text" x="1587" y="1000">possibilities</text>
    <text class="skill-text" x="1587" y="1048">beyond</text>
    <text class="skill-text" x="1587" y="1095">what you know</text>
  </g>

  <!-- Listening panel -->
  <g class="panel panel--listening">
    <path class="outline outline--dashed" d="M638,1548 L590,1640 C575,1670 578,1690 595,1710"/>
    <path class="outline" d="M658,1512 L735,1378 C752,1356 775,1350 800,1360 Q965,1422 1140,1355 C1165,1345 1192,1352 1208,1375 L1282,1498"/>
    <path class="outline outline--dashed" d="M1302,1534 L1355,1625 C1372,1660 1372,1685 1352,1705"/>
    <path class="arc arc--green" d="M600,1710 Q965,1892 1345,1705"/>
    <circle class="node" cx="648" cy="1530" r="18"/>
    <circle class="node" cx="1292" cy="1516" r="18"/>
    <line class="pointer" x1="632" y1="1520" x2="580" y2="1488"/>
    <line class="pointer" x1="1308" y1="1505" x2="1345" y2="1480"/>
    <rect x="925" y="1435" width="100" height="83" rx="24" fill="var(--green)" role="img" aria-label="Person listening to sound icon"/>
    <text class="skill-title skill-title--green" x="973" y="1578">Listening:</text>
    <text class="skill-text skill-text--large" x="973" y="1636">Seek to</text>
    <text class="skill-text skill-text--large" x="973" y="1681">understand</text>
    <text class="skill-text skill-text--large" x="973" y="1726">before speaking</text>
  </g>

  <!-- Connecting captions -->
  <g class="captions">
    <text class="caption" x="488" y="488">Your positive actions</text>
    <text class="caption" x="488" y="517">lead to curiosity</text>
    <text class="caption" x="488" y="545">about what else</text>
    <text class="caption" x="488" y="573">is possible</text>

    <text class="caption" x="1420" y="513">Your imagination</text>
    <text class="caption" x="1420" y="541">can spark</text>
    <text class="caption" x="1420" y="570">positive action</text>

    <text class="caption" x="508" y="1402">Your curiosity</text>
    <text class="caption" x="508" y="1430">allows you</text>
    <text class="caption" x="508" y="1458">to listen</text>

    <text class="caption" x="1408" y="1386">Your listening allows</text>
    <text class="caption" x="1408" y="1414">you to take in new</text>
    <text class="caption" x="1408" y="1442">information</text>
  </g>
</svg>
</body>
</html>
```